Company or website name
- www.brambletonhiregroup.example
- Links to the website
- Brambleton Hire Group
- Describe your company and organization and target audience
- We are a full service executive recruiting and staffing company. We work within all vertical markets within the US.
- The design should have the following
- Please ensure to include colors of the logo but feel free to include other colors as well to enhance the brochure. I'm looking for a single 8.5 x 11 inch brochure with front and back. The back will have more specific information while the front will be more a space for photos and general information on our company.
- Other Facts

```html
<!DOCTYPE html>
<html lang="en">
<head>
<meta charset="utf-8">
<title>Brambleton Hire Group – Brochure Spread</title>
<link rel="stylesheet" href="https://fonts.googleapis.com/css2?family=Arimo:wght@400;700&family=Montserrat:wght@600;700&family=Open+Sans:wght@400;600&display=swap">
<style>
:root{
  --teal:#3a7a90;
  --teal-dark:#2f6a7e;
  --ink:#1c1c1c;
  --black:#151515;
  --cream:#f6ee9e;
  --white:#ffffff;
  --muted:#3a3a3a;
}
*{margin:0;padding:0;box-sizing:border-box}
html,body{width:1200px;height:798px;overflow:hidden;background:var(--white)}
.spread{position:relative;width:1200px;height:798px;background:var(--white);font-family:"Open Sans",Arial,sans-serif;color:var(--ink)}
.abs{position:absolute}

/* top panels */
.photo-team{left:11px;top:101px;width:354px;height:233px;background:linear-gradient(135deg,#e6e8ea 0%,#c9b6a4 40%,#6f8fa8 70%,#dfe3e6 100%)}
.photo-meeting{left:628px;top:106px;width:572px;height:357px;background:linear-gradient(120deg,#eef0f2 0%,#d9c2b4 35%,#f4f4f4 55%,#6a5e58 80%,#2a2a2e 100%)}

.who-tag{left:367px;top:45px;width:188px;height:30px;background:var(--teal);color:var(--white);font-family:"Montserrat",Arial,sans-serif;font-weight:700;font-size:16px;letter-spacing:.3px;display:flex;align-items:center;justify-content:center}

.brand{left:705px;top:26px;width:214px;height:56px;display:flex;align-items:center;gap:9px;padding-left:8px;background:var(--white)}
.brand-dot{width:38px;height:38px;border-radius:50%;background:var(--teal-dark);flex:none}
.brand-name{font-family:"Arimo",Arial,sans-serif;font-weight:700;font-size:15px;line-height:1.1;color:var(--teal-dark)}

.intro{left:11px;top:352px;width:356px;font-size:8.3px;line-height:11.6px;color:var(--muted);text-align:justify}
.intro p+p{margin-top:9px}

.column{left:378px;top:89px;width:168px;font-size:7.1px;line-height:10.3px;color:var(--muted);text-align:justify}
.column h3{font-size:7.6px;font-weight:600;color:var(--ink);margin-bottom:2px;text-align:left}
.column section+section{margin-top:30px}

/* bottom band */
.band{left:0;top:468px;width:1200px;height:318px;background:var(--teal)}
.band-rule{left:628px;top:468px;width:572px;height:18px;background:var(--black)}

.connect{left:0;top:508px;width:442px;height:38px;background:var(--black);color:var(--white);font-family:"Montserrat",Arial,sans-serif;font-weight:700;font-size:17px;display:flex;align-items:center;padding-left:168px;letter-spacing:.3px}

.contact{font-family:"Arimo",Arial,sans-serif;color:var(--white);font-size:11.6px;line-height:14.5px}
.contact b{font-weight:700}
.office{left:111px;top:586px}
.phone{left:111px;top:665px}
.fax{left:111px;top:709px}
.email{left:347px;top:586px}
.web{left:347px;top:614px}
.social-a{left:347px;top:673px}
.social-b{left:347px;top:701px}
.indent{padding-left:42px}

.hook{left:640px;top:504px;width:512px;text-align:right;color:var(--white);font-family:"Arimo",Arial,sans-serif;font-weight:700;font-size:25px;letter-spacing:-.2px;padding-right:18px}
.headline{left:640px;top:536px;width:512px;text-align:right;color:var(--cream);font-family:"Arimo",Arial,sans-serif;font-weight:700;font-size:66px;line-height:72px;letter-spacing:-2px}
.mission{left:640px;top:623px;width:515px;color:var(--white);font-size:11.4px;line-height:14.8px;text-align:justify}
.mission-rule{left:640px;top:707px;width:512px;height:2px;background:var(--cream)}
.site{left:640px;top:718px;width:512px;text-align:right;color:var(--cream);font-family:"Arimo",Arial,sans-serif;font-weight:700;font-size:16px}
</style>
</head>
<body>
<main class="spread">

  <div class="abs photo-team" role="img" aria-label="Photo of a young team gathered around a computer monitor"></div>

  <div class="abs who-tag">WHO WE ARE?</div>

  <div class="abs column">
    <section>
      <h3>OUR APPROACH TO HIRING</h3>
      <p>We place skilled people in roles that fit their strengths and goals. Our recruiters listen first, study each opening in detail and then search widely for candidates who match the culture as well as the job. Every client gets one dedicated contact who follows the search from the first call to the first day. We check references, confirm skills and prepare each candidate for the interview. The result is a shorter hiring cycle, fewer surprises and teams that stay together longer. We measure success by the placements that last.</p>
    </section>
    <section>
      <h3>SERVING EVERY INDUSTRY</h3>
      <p>From finance and health care to logistics and technology, we recruit across every vertical market in the country. Our network includes executives, managers and specialists ready for their next move. We offer direct hire, contract and contract to hire options so each client can choose the model that suits its budget and timeline. Candidates receive honest advice, clear feedback and support through every stage. Employers receive a shortlist of qualified people, not a pile of resumes. That focus keeps our partners coming back year after year.</p>
    </section>
  </div>

  <div class="abs intro">
    <p>We recognize that consistency is critical to the achievement of our mission. We always act with a sense of urgency, respond quickly to client needs, and meet our commitments to provide only the best staffing services.</p>
    <p>We strive for excellence in everything we do. We encourage innovative thinking that enhances our ability to reduce labor costs and allows us to find talent for hard to fill positions.</p>
  </div>

  <div class="abs brand">
    <span class="brand-dot"></span>
    <span class="brand-name">BRAMBLETON<br>HIRE GROUP</span>
  </div>

  <div class="abs photo-meeting" role="img" aria-label="Photo of three smiling business professionals looking at a laptop screen"></div>

  <div class="abs band"></div>
  <div class="abs band-rule"></div>

  <div class="abs connect">STAY CONNECTED WITH US</div>

  <div class="abs contact office"><b>HEAD OFFICE:</b><br>suite 210, 48 Harlow Lane<br>Fresno, CA, United States</div>
  <div class="abs contact phone"><b>PHONE:</b> +1 555-0134-998<br><span class="indent">+1 555-0187-986</span></div>
  <div class="abs contact fax"><b>FAX:</b> +1 555-0134-933</div>
  <div class="abs contact email"><b>EMAIL:</b> info@brambletonhiregroup.example</div>
  <div class="abs contact web"><b>WEB:</b> www.brambletonhiregroup.example</div>
  <div class="abs contact social-a">social.example/<b>Brambleton</b></div>
  <div class="abs contact social-b">news.example/<b>Brambleton</b></div>

  <div class="abs hook">Whatever you're looking for</div>
  <div class="abs headline">we've got it</div>
  <p class="abs mission">At Brambleton Hire Group, our mission is to match employers with employees to form successful work relationships. We succeed in our mission by providing excellent service to our clients and candidates, consistently meeting established expectations, and setting and maintaining the highest standards and ethics demonstrated in the employment services industry.</p>
  <div class="abs mission-rule"></div>
  <div class="abs site">www.brambletonhiregroup.example</div>

</main>
</body>
</html>
```